Upscale Wine Cooler/Ready to drink Can Design

We need to design the branding and packaging for a new wine cooler that will be sold in a can. We are also looking for the brand name at this point, so you can be as creative as you can!

The product will have 3 flavours (Cavoni Spritz, Ginger-Lime Spritz, Raspeberry-Mimosa) and will be made of genuine high quality European Wine, with natural flavours

Can dimensions : Height 157 mm ; Diameter : 58 mm
Updates

Need extra days to review

Target Market(s)

Females 19 to 35, who are looking for an alternative to the traditional alcoholic beverages, and who want to drink an upscale and "classy" beverage

Colors

Designer to choose colors to be used in the design.

Requirements
Must have
• Modern, attractive and upscale look
• Brand name
• 3 different cans for each of the flavours : Cavoni Spritz, Ginger-Lime Spritz, Raspeberry-Mimosa
• 355 ml
• 5% alc./vol.

```html
<!DOCTYPE html>
<html lang="en">
<head>
<meta charset="utf-8">
<title>Belvigne Wine Based Spritzer – Can Range</title>
<link href="https://fonts.googleapis.com/css2?family=Patrick+Hand&display=swap" rel="stylesheet">
<style>
  :root {
    --stage: #f3eee6;
    --silver: #b9b9bb;
    --silver-light: #e4e4e6;
    --brand-plum: #7b2a40;
    --white: #ffffff;

    --ginger-band: #d6d4ab;
    --ginger-label: #ecebd6;
    --ginger-base: #a6a27a;
    --ginger-flavour: #6f8f3a;

    --cavoni-band: #e47a3a;
    --cavoni-label: #efcfc2;
    --cavoni-base: #dc7a3c;
    --cavoni-flavour: #7b2a40;

    --rasp-band: #8c1e30;
    --rasp-label: #dcc8cd;
    --rasp-base: #7c1a2a;
    --rasp-flavour: #7b2a40;

    --sky: #b9bcc0;
    --hills: #8b8f70;
    --vines: #5d7040;
  }
  * { margin: 0; padding: 0; box-sizing: border-box; }
  html, body { width: 1200px; height: 494px; overflow: hidden; }
  body {
    background: var(--stage);
    font-family: "Patrick Hand", cursive;
  }
  .can-range {
    position: relative;
    width: 1200px;
    height: 494px;
    display: flex;
    justify-content: center;
    align-items: center;
    gap: 24px;
  }
  .can-label { width: 170px; height: 430px; display: block; }
  .can-label text { font-family: "Patrick Hand", cursive; }
  .range-tag { font-size: 14px; fill: var(--white); letter-spacing: 0.3px; }
  .brand-name { font-size: 42px; fill: var(--brand-plum); }
  .flavour-name { font-size: 18px; }
  .spec { font-size: 11.5px; fill: var(--white); }
  .silver-line { fill: none; stroke: var(--silver); stroke-width: 3; }
  .silver-band { fill: var(--silver-light); stroke: var(--silver); stroke-width: 1; }

  .can-ginger .top-band { fill: var(--ginger-band); }
  .can-ginger .label-field { fill: var(--ginger-label); }
  .can-ginger .base-band { fill: var(--ginger-base); }
  .can-ginger .flavour-name { fill: var(--ginger-flavour); }

  .can-cavoni .top-band { fill: var(--cavoni-band); }
  .can-cavoni .label-field { fill: var(--cavoni-label); }
  .can-cavoni .base-band { fill: var(--cavoni-base); }
  .can-cavoni .flavour-name { fill: var(--cavoni-flavour); }

  .can-raspberry .top-band { fill: var(--rasp-band); }
  .can-raspberry .label-field { fill: var(--rasp-label); }
  .can-raspberry .base-band { fill: var(--rasp-base); }
  .can-raspberry .flavour-name { fill: var(--rasp-flavour); }
</style>
</head>
<body>
<main class="can-range">

  <!-- Ginger-Lime Spritz -->
  <svg class="can-label can-ginger" viewBox="0 0 170 430" xmlns="http://www.w3.org/2000/svg">
    <defs>
      <linearGradient id="scene-ginger" x1="0" y1="0" x2="0" y2="1">
        <stop offset="0" stop-color="var(--sky)"/>
        <stop offset="0.35" stop-color="var(--hills)"/>
        <stop offset="1" stop-color="var(--vines)"/>
      </linearGradient>
    </defs>
    <rect class="label-field" width="170" height="430" rx="6"/>
    <path class="top-band" d="M0 0 H170 V40 C120 30 60 54 0 44 Z"/>
    <path class="silver-line" d="M0 50 C60 60 120 36 170 46"/>
    <text class="range-tag" x="85" y="27" text-anchor="middle">WINE BASED SPRITZER</text>
    <text class="brand-name" x="85" y="122" text-anchor="middle">Belvigne</text>
    <text class="flavour-name" x="85" y="172" text-anchor="middle">Ginger-Lime Spritz</text>
    <rect class="silver-band" x="0" y="186" width="170" height="5"/>
    <g role="img" aria-label="Vineyard landscape with a ginger-lime spritz cocktail glass">
      <path fill="url(#scene-ginger)" d="M0 191 H170 V372 C120 384 60 360 0 370 Z"/>
    </g>
    <path class="silver-line" d="M0 372 C60 362 120 386 170 374"/>
    <path class="base-band" d="M0 376 C60 366 120 390 170 378 V430 H0 Z"/>
    <text class="spec" x="10" y="413">5% ALC.VOL</text>
    <text class="spec" x="160" y="413" text-anchor="end">355ml</text>
  </svg>

  <!-- Cavoni Spritz -->
  <svg class="can-label can-cavoni" viewBox="0 0 170 430" xmlns="http://www.w3.org/2000/svg">
    <defs>
      <linearGradient id="scene-cavoni" x1="0" y1="0" x2="0" y2="1">
        <stop offset="0" stop-color="var(--sky)"/>
        <stop offset="0.35" stop-color="var(--hills)"/>
        <stop offset="1" stop-color="var(--vines)"/>
      </linearGradient>
    </defs>
    <rect class="label-field" width="170" height="430" rx="6"/>
    <path class="top-band" d="M0 0 H170 V40 C120 30 60 54 0 44 Z"/>
    <path class="silver-line" d="M0 50 C60 60 120 36 170 46"/>
    <text class="range-tag" x="85" y="27" text-anchor="middle">WINE BASED SPRITZER</text>
    <text class="brand-name" x="85" y="122" text-anchor="middle">Belvigne</text>
    <text class="flavour-name" x="85" y="172" text-anchor="middle">Cavoni Spritz</text>
    <rect class="silver-band" x="0" y="186" width="170" height="5"/>
    <g role="img" aria-label="Vineyard landscape with an orange Cavoni spritz in a wine glass">
      <path fill="url(#scene-cavoni)" d="M0 191 H170 V372 C120 384 60 360 0 370 Z"/>
    </g>
    <path class="silver-line" d="M0 372 C60 362 120 386 170 374"/>
    <path class="base-band" d="M0 376 C60 366 120 390 170 378 V430 H0 Z"/>
    <text class="spec" x="10" y="413">5% ALC.VOL</text>
    <text class="spec" x="160" y="413" text-anchor="end">355ml</text>
  </svg>

  <!-- Raspberry-Mimosa -->
  <svg class="can-label can-raspberry" viewBox="0 0 170 430" xmlns="http://www.w3.org/2000/svg">
    <defs>
      <linearGradient id="scene-rasp" x1="0" y1="0" x2="0" y2="1">
        <stop offset="0" stop-color="var(--sky)"/>
        <stop offset="0.35" stop-color="var(--hills)"/>
        <stop offset="1" stop-color="var(--vines)"/>
      </linearGradient>
    </defs>
    <rect class="label-field" width="170" height="430" rx="6"/>
    <path class="top-band" d="M0 0 H170 V40 C120 30 60 54 0 44 Z"/>
    <path class="silver-line" d="M0 50 C60 60 120 36 170 46"/>
    <text class="range-tag" x="85" y="27" text-anchor="middle">WINE BASED SPRITZER</text>
    <text class="brand-name" x="85" y="122" text-anchor="middle">Belvigne</text>
    <text class="flavour-name" x="85" y="172" text-anchor="middle">Raspberry-Mimosa</text>
    <rect class="silver-band" x="0" y="186" width="170" height="5"/>
    <g role="img" aria-label="Vineyard landscape with a raspberry mimosa in a glass">
      <path fill="url(#scene-rasp)" d="M0 191 H170 V372 C120 384 60 360 0 370 Z"/>
    </g>
    <path class="silver-line" d="M0 372 C60 362 120 386 170 374"/>
    <path class="base-band" d="M0 376 C60 366 120 390 170 378 V430 H0 Z"/>
    <text class="spec" x="10" y="413">5% ALC.VOL</text>
    <text class="spec" x="160" y="413" text-anchor="end">355ml</text>
  </svg>

</main>
</body>
</html>
```